Redesign of Website

We need an overhaul of our website. I've attached our current logo files. Please visit www.pelvorix.com for our current website for information about our company. We are looking for the same type of website (information-based only) so no need for any online store, payments, interactive stuff or anything like that...basically looking for a fresh new look! Also please make sure this design will be mobile-friendly. Thanks!

```html
<!DOCTYPE html>
<html lang="en">
<head>
<meta charset="utf-8">
<title>Pelvorix Consultants</title>
<link rel="stylesheet" href="https://fonts.googleapis.com/css2?family=Arimo:wght@400;700&display=swap">
<style>
:root{
  --brand-blue:#0b4a92;
  --text-grey:#58595b;
  --nav-grey:#5d6266;
  --band-grey:#f3f3f3;
  --footer-grey:#5f6366;
  --hero-green:#cfeec3;
  --white:#ffffff;
}
*{box-sizing:border-box;margin:0;padding:0}
html,body{width:1200px;height:1130px;overflow:hidden;background:var(--white);font-family:"Arimo",Arial,sans-serif}
.page{position:relative;width:1200px;height:1130px}
.site-header{position:absolute;top:0;left:0;width:1200px;height:60px}
.brand{position:absolute;left:123px;top:14px;font-size:28px;font-weight:700;color:var(--brand-blue);letter-spacing:0.5px}
.top-nav{position:absolute;right:119px;top:22px;display:flex;gap:23px}
.top-nav a{font-size:15px;font-weight:700;color:var(--nav-grey);text-decoration:none;letter-spacing:0.3px}
.top-nav a.active{color:var(--brand-blue)}
.hero{position:absolute;top:61px;left:0;width:1200px;height:400px;overflow:hidden}
.hero-photo{position:absolute;inset:0;background:linear-gradient(100deg,#4e5558 0%,#5b4d45 35%,#3a3632 60%,#25303f 100%)}
.hero-title{position:absolute;left:121px;top:118px;font-size:30px;line-height:36px;font-weight:700;color:var(--hero-green);letter-spacing:0.4px}
.hero-text{position:absolute;left:121px;top:202px;width:720px;font-size:15px;line-height:18px;color:var(--white)}
.hero-more{position:absolute;left:121px;top:251px;width:80px;height:29px;border-radius:15px;background:var(--brand-blue);color:var(--white);font-size:15px;font-weight:700;text-align:center;line-height:29px}
.hero-arrows{position:absolute;left:999px;top:311px}
.intro-band{position:absolute;left:120px;top:461px;width:960px;height:69px;background:var(--band-grey)}
.intro-band h1{position:absolute;left:1px;top:34px;font-size:27px;font-weight:700;color:var(--brand-blue)}
.content{position:absolute;left:121px;top:551px;width:700px}
.content p{font-size:18px;line-height:23.7px;color:var(--text-grey);margin-bottom:18px}
.sidebar{position:absolute;left:864px;top:548px;width:217px}
.sidebar h2{text-align:center;font-size:25px;font-weight:400;color:var(--brand-blue);height:37px}
.side-box{border:1.5px solid var(--brand-blue);border-radius:8px;padding:8px 5px 14px;height:248px}
.side-item{position:relative;height:25px;border-radius:4px;background:var(--nav-grey);color:var(--white);font-size:11px;font-weight:700;line-height:25px;padding-left:12px;margin-bottom:11px}
.side-item.open{background:var(--brand-blue);margin-bottom:4px}
.side-item svg{position:absolute;right:9px;top:4px}
.sub-list{list-style:none;padding-left:13px}
.sub-list li{font-size:10px;line-height:18px;color:var(--text-grey);letter-spacing:0.1px}
.footer{position:absolute;left:0;top:1070px;width:1200px;height:42px;background:var(--footer-grey);color:var(--white);font-size:12px;font-weight:700;text-align:center;line-height:42px}
.footer-strip{position:absolute;left:0;top:1112px;width:1200px;height:18px;background:var(--brand-blue);color:var(--white);font-size:9px;font-weight:700;text-align:center;line-height:18px}
</style>
</head>
<body>
<div class="page">
  <header class="site-header">
    <div class="brand">PELVORIX</div>
    <nav class="top-nav">
      <a class="active" href="#">HOME</a>
      <a href="#">ABOUT</a>
      <a href="#">CONTACT</a>
      <a href="#">SERVICES</a>
    </nav>
  </header>

  <section class="hero">
    <div class="hero-photo" role="img" aria-label="Brick house under construction with scaffolding and a worker on site"></div>
    <h2 class="hero-title">CONSTRUCTION<br>FUNDING INSPECTIONS</h2>
    <p class="hero-text">Lending institutions rarely have employees with the expertise needed to evaluate multiple stages of site construction and ensure that projects are being completed as detailed in the plans and specifications</p>
    <div class="hero-more">MORE</div>
    <svg class="hero-arrows" width="84" height="38" viewBox="0 0 84 38">
      <circle cx="18" cy="19" r="17" fill="none" stroke="#fff" stroke-width="2"/>
      <polyline points="21,11 15,19 21,27" fill="none" stroke="#fff" stroke-width="2"/>
      <circle cx="64" cy="19" r="17" fill="none" stroke="#fff" stroke-width="2"/>
      <polyline points="61,11 67,19 61,27" fill="none" stroke="#fff" stroke-width="2"/>
    </svg>
  </section>

  <div class="intro-band"><h1>Pelvorix.com – Pelvorix Consultants, INC.</h1></div>

  <main class="content">
    <p>With over 25 years experience we provide customized and comprehensive inspection services to financial institutions involved in construction and loan management in New York, New Jersey, Pennsylvania and surrounding areas.</p>
    <p>The firm’s professional staff bring years of engineering, environmental, building, and real estate experience to work for our clients.</p>
    <p>Pelvorix provides our clients with in-depth plan &amp; cost, construction funding, environmental and property condition reports.</p>
    <p>Pelvorix will give you the essential facts that are critical for solid business decision making and ongoing loan management.</p>
    <p>Pelvorix Consultants’ projects range from single family homes to $30,000,000 mid-rise buildings to $60,000,000 casino renovation projects. Our clients have come to think of us as part of their trusted team. They turn to us to evaluate plans, costs and approvals before they commit to a construction loan; and enlist our services throughout the construction process to ensure that all phases of the project are funded properly and documented accordingly. Pelvorix understands the delicate balance required in order to protect the client’s position and simultaneously keep their costumers satisfied.</p>
  </main>

  <aside class="sidebar">
    <h2>NAVIGATION</h2>
    <div class="side-box">
      <div class="side-item">HOME</div>
      <div class="side-item">ABOUT</div>
      <div class="side-item">CONTACT</div>
      <div class="side-item open">SERVICES
        <svg width="17" height="17" viewBox="0 0 17 17"><circle cx="8.5" cy="8.5" r="8" fill="#fff"/><path d="M8.5 4v9M4 8.5h9" stroke="#0b4a92" stroke-width="2.2"/></svg>
      </div>
      <ul class="sub-list">
        <li>Property Condition Reports</li>
        <li>Plan &amp; Cost Reviews</li>
        <li>Construction Funding Inspections</li>
        <li>Environmental Transaction Screens</li>
        <li>Phase 1 Environmental Assessment</li>
      </ul>
    </div>
  </aside>

  <footer class="footer">Copyright 2014 | Pelvorix.com | 418 Ridgeline Rd #112 Halden Township, NJ 07790 | 555-014-2790</footer>
  <div class="footer-strip">Pelvorix.com</div>
</div>
</body>
</html>
```